Internationales Familienunternehmen sucht Designvorschläge für Broschüre/Folder
Zielgruppe
Unser Unternehmen besteht aus 4 aktiven Sparten:
gastrosystems | elektrosystems | servicepartner | morafi kavum crafts
Alle Sparten sollen mit einem Layout bedient werden. Ziel wäre es aber z.B. auf der Titelseite im oberen Bereich die jeweiligen Sparten erkennen zu können und das jeweilige Prospektthema klein. Sodass man z.B. in einem Prospektständer die verschiedenen Prospekte auf einen Griff unterscheiden udn entnehmen kann.
Das Design muss verschiedenen Zielgruppen gefallen, daher muss das Layout modern, jung und dem neuen Logo entsprechend sein.
Aufgabenstellung
Wir haben unser Logo mit Anfang 2014 einem kompletten Redesign unterzogen und benötigen jetzt ein modernes und ansprechendes "passendes" Layout für unsere Produktbroschüren und -folder. Gesucht ist also Layoutvorschlag für Umschlag und Innenteil zur Präsentation von Produkten, Referenzen und natürlich entsprechenden Textflächen.
Als Ideenvolage kann unsere derzeit entstehende Website dienen: http://new.kavum.net/
Bitte NICHT (!!!) an unserer bestehenden Website orientieren. www.kavum.net ist nur noch kurze Zeit online!!! ACHTUNG!!!

```html
<!DOCTYPE html>
<html lang="de">
<head>
<meta charset="utf-8">
<title>Broschüren-Titelseiten – Sparten</title>
<link rel="stylesheet" href="https://fonts.googleapis.com/css2?family=Orbitron:wght@700&family=Crimson+Text&display=swap">
<style>
  :root {
    --stage: #3b3d40;
    --paper: #ffffff;
    --ink: #1d1d1b;
    --red: #a51d24;
    --navy: #3d3f57;
    --yellow: #fde03e;
    --teal: #1b7f8c;
    --logo-ring: #ef8a2a;
  }
  * { margin: 0; padding: 0; box-sizing: border-box; }
  html, body { width: 1200px; height: 528px; overflow: hidden; background: var(--stage); }
  .stage { position: relative; width: 1200px; height: 528px; }

  .cover {
    position: absolute; top: 100px; width: 240px; height: 341px;
    background: var(--paper); overflow: hidden;
  }
  .cover--gastro  { left: 50px;  --accent: var(--red); }
  .cover--events  { left: 335px; --accent: var(--navy); }
  .cover--service { left: 624px; --accent: var(--yellow); }
  .cover--elektro { left: 915px; --accent: var(--teal); }

  .cover__tab { position: absolute; left: 0; top: 0; width: 16px; height: 89px; background: var(--accent); }

  .brand {
    position: absolute; left: 168px; top: 36px;
    display: flex; align-items: center; gap: 4px;
  }
  .brand__dot { width: 12px; height: 12px; border-radius: 50%; background: var(--logo-ring); }
  .brand__name {
    font-family: "Orbitron", sans-serif; font-weight: 700; font-size: 11px;
    color: var(--ink); letter-spacing: .5px;
  }

  .cover__photo {
    position: absolute; left: 95px; top: 83px; width: 146px; height: 103px;
    border: 2px solid var(--accent);
  }
  .cover--elektro .cover__photo { border-color: #111; }
  .photo--taps    { background: linear-gradient(135deg, #3a1c0c, #b77a2e 45%, #6b3a14); }
  .photo--party   { background: linear-gradient(120deg, #2541a8, #d9a98b 45%, #f0d7b8 70%, #3d62c4); }
  .photo--beer    { background: linear-gradient(180deg, #2a1a10, #5b3218 50%, #c0612a); }
  .photo--store   { background: linear-gradient(180deg, #c9ccd2, #9a5b4a 55%, #8d9198); }

  .cover__title {
    position: absolute; left: 32px; top: 203px;
    font-family: "Orbitron", sans-serif; font-weight: 700; font-size: 8.6px;
    letter-spacing: .6px; text-transform: uppercase; color: var(--accent); white-space: nowrap;
  }
  .cover__subtitle {
    position: absolute; left: 32px; top: 217px;
    font-family: "Orbitron", sans-serif; font-weight: 700; font-size: 5.6px;
    letter-spacing: .5px; text-transform: uppercase; color: var(--accent);
  }
  .cover__text {
    position: absolute; left: 73px; top: 249px; width: 147px;
    font-family: "Crimson Text", serif; font-size: 6.3px; line-height: 8.2px;
    color: var(--ink); text-align: justify; hyphens: auto;
  }

  .cover__foot-block { position: absolute; left: 0; top: 313px; width: 54px; height: 28px; background: var(--accent); }
  .cover__foot-band  { position: absolute; left: 0; top: 327px; width: 240px; height: 14px; background: var(--accent); }
</style>
</head>
<body>
<main class="stage">

  <article class="cover cover--gastro">
    <div class="cover__tab"></div>
    <div class="brand"><span class="brand__dot"></span><span class="brand__name">kavum</span></div>
    <div class="cover__photo photo--taps" role="img" aria-label="Zapfhähne an einer Bartheke"></div>
    <h1 class="cover__title">morafi kavum crafts</h1>
    <h2 class="cover__subtitle">Untertitel</h2>
    <p class="cover__text">Kurztext, Ictiur, sit faceperrum et dita veriati oratibus coreicta dolores eos ut odigent acillaut quas sequationse ventus, arcia nissitatur siti as apit, utem ipsam, invelenimus nonectur? Orioritius anda que aut hario cusanto ommo voluptaeptus ut ventur, alissum nonsequ aecatata voluptaqui officia nduciae nonse oditatquunt, ut elessum veribusda dolesti ntiisti onsequae il et dolo cum est ra nonsecum qui quaerum harum expelessi occum ima verit aut repeliatur aut pliam f</p>
    <div class="cover__foot-block"></div><div class="cover__foot-band"></div>
  </article>

  <article class="cover cover--events">
    <div class="cover__tab"></div>
    <div class="brand"><span class="brand__dot"></span><span class="brand__name">kavum</span></div>
    <div class="cover__photo photo--party" role="img" aria-label="Drei Frauen stoßen mit Gläsern an"></div>
    <h1 class="cover__title">morafi kavum crafts</h1>
    <h2 class="cover__subtitle">Untertitel</h2>
    <p class="cover__text">Kurztext, Ictiur, sit faceperrum et dita veriati oratibus coreicta dolores eos ut odigent acillaut quas sequationse ventus, arcia nissitatur siti as apit, utem ipsam, invelenimus nonectur? Orioritius anda que aut hario cusanto ommo voluptaeptus ut ventur, alissum nonsequ aecatata voluptaqui officia nduciae nonse oditatquunt, ut elessum veribusda dolesti ntiisti onsequae il et dolo cum est ra nonsecum qui quaerum harum expelessi occum ima verit aut repeliatur aut pliam f</p>
    <div class="cover__foot-block"></div><div class="cover__foot-band"></div>
  </article>

  <article class="cover cover--service">
    <div class="cover__tab"></div>
    <div class="brand"><span class="brand__dot"></span><span class="brand__name">kavum</span></div>
    <div class="cover__photo photo--beer" role="img" aria-label="Bierflaschen und Gläser auf einer Theke"></div>
    <h1 class="cover__title">Servicepartner</h1>
    <h2 class="cover__subtitle">Untertitel</h2>
    <p class="cover__text">Kurztext, Ictiur, sit faceperrum et dita veriati oratibus coreicta dolores eos ut odigent acillaut quas sequationse ventus, arcia nissitatur siti as apit, utem ipsam, invelenimus nonectur? Orioritius anda que aut hario cusanto ommo voluptaeptus ut ventur, alissum nonsequ aecatata voluptaqui officia nduciae nonse oditatquunt, ut elessum veribusda dolesti ntiisti onsequae il et dolo cum est ra nonsecum qui quaerum harum expelessi occum ima verit aut repeliatur aut pliam f</p>
    <div class="cover__foot-block"></div><div class="cover__foot-band"></div>
  </article>

  <article class="cover cover--elektro">
    <div class="cover__tab"></div>
    <div class="brand"><span class="brand__dot"></span><span class="brand__name">kavum</span></div>
    <div class="cover__photo photo--store" role="img" aria-label="Lagerhalle mit Paletten und Regalen"></div>
    <h1 class="cover__title">Elektrosystems</h1>
    <h2 class="cover__subtitle">Untertitel</h2>
    <p class="cover__text">Kurztext, Ictiur, sit faceperrum et dita veriati oratibus coreicta dolores eos ut odigent acillaut quas sequationse ventus, arcia nissitatur siti as apit, utem ipsam, invelenimus nonectur? Orioritius anda que aut hario cusanto ommo voluptaeptus ut ventur, alissum nonsequ aecatata voluptaqui officia nduciae nonse oditatquunt, ut elessum veribusda dolesti ntiisti onsequae il et dolo cum est ra nonsecum qui quaerum harum expelessi occum ima verit aut repeliatur aut pliam f</p>
    <div class="cover__foot-block"></div><div class="cover__foot-band"></div>
  </article>

</main>
</body>
</html>
```